Website redesign for job agency recruitment

Please refer to the attached document, “Harbor Work Portal Outline,” for comprehensive details regarding the scope, objectives, and requirements of this website redesign project.

For imagery you can use images from this website https://www.pixvaultmedia.com or any other you regularly use.

Target Market(s)

Jobseekers and Companies looking for general labour

Industry/Entity Type

Services: Oil, Gas and Mining, Administrative, Construction and Trades, Warehouse and Logistics and, Manufacturing.

Number of Pages Required

5+ page

Font styles to use
Serif
Other font styles liked:
• Inter, Open-Sans or similar.

Requirements
Must have
• The requirements highlighted in the Word document attached. The final design needs to be provided in Figma including all viewports (Desktop, mobiel and tablet)
Should not have
• Website we like as a reference: www.beltonworkforceinc.com, www.veltaworkforce.com, www.zplacer.com, www.brimwellworkforce.com, www.9tworkcrew.com, www.hiringonthemove.ca

```html
<!DOCTYPE html>
<html lang="en">
<head>
<meta charset="utf-8">
<title>Harbor Work Agency – Candidates &amp; Employers Pages</title>
<link href="https://fonts.googleapis.com/css2?family=Barlow+Semi+Condensed:wght@500;600;700&family=Inter:wght@400;500;600;700&display=swap" rel="stylesheet">
<style>
:root{
  --board:#e8e8e8;
  --ink:#1b1b1b;
  --text:#3a3a3a;
  --navy:#0c2448;
  --blue:#143e8f;
  --link-blue:#1c4fb0;
  --yellow:#f5c20f;
  --yellow-deep:#e9ad08;
  --card:#f4f4f4;
  --card-line:#e4e4e4;
  --foot-text:#b8c3d6;
  --white:#ffffff;
}
*{box-sizing:border-box;margin:0;padding:0}
html,body{width:1200px;height:1132px;overflow:hidden;background:var(--board)}
body{font-family:"Inter",Arial,sans-serif;color:var(--text)}
.board{position:relative;width:1988px;height:1876px;transform:scale(.6037);transform-origin:0 0}
.board-label{position:absolute;font-family:"Inter",Arial,sans-serif;font-weight:700;font-size:18px;color:var(--ink);letter-spacing:.2px}
.page{position:absolute;width:840px;background:var(--white);overflow:hidden}
.page--candidates{left:152px;top:142px;height:1607px}
.page--employers{left:1039px;top:142px;height:1048px}
.abs{position:absolute}

/* header */
.brand{position:absolute;left:78px;top:14px;display:flex;align-items:center;gap:8px;width:120px}
.brand-mark{width:30px;height:30px;border-radius:50%;background:var(--navy);flex:none}
.brand-name{font-family:"Barlow Semi Condensed",sans-serif;font-weight:700;font-size:14px;line-height:15px;color:var(--navy)}
.topbar-phone{position:absolute;left:376px;top:0;width:222px;height:41px;background:var(--blue);clip-path:polygon(7px 0,100% 0,calc(100% - 8px) 100%,0 100%);display:flex;align-items:center;padding-left:32px;gap:10px;color:var(--white);font-family:"Barlow Semi Condensed",sans-serif;font-weight:600;font-size:13px}
.topbar-register{position:absolute;left:586px;top:0;width:254px;height:41px;background:linear-gradient(90deg,var(--yellow-deep),var(--yellow));clip-path:polygon(10px 0,100% 0,100% 100%,0 100%);display:flex;align-items:center;padding-left:54px;gap:12px;color:var(--ink);font-family:"Barlow Semi Condensed",sans-serif;font-weight:600;font-size:13px}
.main-nav a{position:absolute;top:62px;font-family:"Barlow Semi Condensed",sans-serif;font-weight:600;font-size:13px;color:var(--ink);text-decoration:none;white-space:nowrap}
.main-nav a.is-active{color:var(--link-blue)}

/* hero */
.hero{position:absolute;left:0;top:93px;width:840px;height:172px}
.hero--candidates{background:linear-gradient(90deg,#3d4450 0%,#6b5a44 22%,#8a7a5c 38%,#9a8a6a 52%,#55606e 66%,#8b6a56 76%,#3a5f88 88%,#2d4a70 100%)}
.hero--employers{background:linear-gradient(180deg,#4f6d96 0%,#3b5578 45%,#22324d 100%)}
.hero-title{position:absolute;left:76px;top:72px;font-family:"Barlow Semi Condensed",sans-serif;font-weight:600;font-size:23px;color:var(--white);letter-spacing:.3px}

/* headings */
.section-title{position:absolute;font-family:"Barlow Semi Condensed",sans-serif;font-weight:600;font-size:24px;line-height:30px;color:var(--ink);white-space:nowrap}
.section-title .accent{background:var(--yellow);padding:0 6px;margin-left:3px}
.body-copy{position:absolute;font-size:11px;line-height:17.5px;color:var(--text)}

/* photos */
.photo{position:absolute}
.photo--round{border-radius:50%}
.photo-frame{position:absolute;border:1px solid var(--yellow)}

/* cards */
.placement-card{position:absolute;top:760px;width:218px;height:120px;background:var(--card);border:1px solid var(--card-line)}
.placement-card svg{position:absolute;left:14px;top:14px}
.placement-card h3{position:absolute;left:52px;top:20px;font-family:"Barlow Semi Condensed",sans-serif;font-weight:600;font-size:14px;color:var(--ink);white-space:nowrap}
.placement-card p{position:absolute;left:14px;top:52px;width:196px;font-size:10.5px;line-height:17.5px;color:var(--text)}
.apply-button{position:absolute;left:150px;top:869px;width:72px;height:20px;background:var(--yellow);font-family:"Barlow Semi Condensed",sans-serif;font-weight:600;font-size:11px;color:var(--ink);display:flex;align-items:center;padding-left:12px}
.apply-button::after,.register-button::after{content:"";position:absolute;right:-1px;top:0;border-style:solid;border-color:transparent transparent var(--blue) transparent}
.apply-button::after{border-width:0 0 12px 6px;top:8px}

/* connect */
.connect-badge{position:absolute;width:60px;height:60px;border-radius:50%;background:var(--yellow);display:flex;align-items:center;justify-content:center}
.connect-title{position:absolute;left:494px;font-family:"Barlow Semi Condensed",sans-serif;font-weight:600;font-size:15px;color:var(--ink)}
.connect-copy{position:absolute;left:494px;width:268px;font-size:10.3px;line-height:16.4px;color:var(--text)}
.connect-copy b{color:var(--ink);font-weight:600}
.connect-copy a{color:var(--blue);font-weight:600;text-decoration:none}

/* register */
.register-button{position:absolute;left:457px;top:678px;width:170px;height:36px;background:var(--yellow);font-family:"Barlow Semi Condensed",sans-serif;font-weight:600;font-size:15px;color:var(--ink);display:flex;align-items:center;padding-left:17px}
.register-button::after{border-width:0 0 22px 10px;top:14px}

/* footer */
.site-footer{position:absolute;left:0;width:840px;height:287px;background:linear-gradient(180deg,#0c2448 0%,#0f2a52 100%)}
.site-footer .divider{position:absolute;top:0;width:1px;height:230px;background:rgba(255,255,255,.06)}
.footer-brand{position:absolute;left:76px;top:58px;width:110px;display:flex;flex-direction:column;align-items:center;gap:8px}
.footer-brand .brand-mark{width:44px;height:44px;background:none;border:2px solid var(--white)}
.footer-brand .brand-name{color:var(--white);text-align:center;font-size:13px}
.social-dot{position:absolute;top:157px;width:22px;height:22px;border-radius:50%;border:1.2px solid var(--foot-text)}
.footer-heading{position:absolute;top:58px;font-family:"Barlow Semi Condensed",sans-serif;font-weight:600;font-size:15px;color:var(--white)}
.footer-heading::after{content:"";position:absolute;left:0;top:24px;width:11px;height:2px;background:var(--yellow)}
.footer-links{position:absolute;top:92px;list-style:none}
.footer-links li{font-size:10.5px;line-height:23.4px;color:var(--foot-text)}
.footer-contact{position:absolute;left:613px;font-size:10.5px;line-height:16px;color:var(--foot-text);display:flex;gap:10px}
.footer-contact svg{flex:none}
.copyright{position:absolute;left:0;top:258px;width:840px;text-align:center;font-size:10px;color:var(--foot-text)}
</style>
</head>
<body>
<div class="board">
  <h2 class="board-label" style="left:152px;top:87px">CANDIDATES</h2>
  <h2 class="board-label" style="left:1039px;top:79px">EMPLOYERS</h2>

  <!-- Candidates page -->
  <section class="page page--candidates">
    <header>
      <div class="brand"><span class="brand-mark"></span><span class="brand-name">Harbor Work Agency Ltd.</span></div>
      <div class="topbar-phone">
        <svg width="14" height="14" viewBox="0 0 24 24"><path fill="#fff" d="M6.6 10.8a15.1 15.1 0 0 0 6.6 6.6l2.2-2.2a1 1 0 0 1 1-.25 11.4 11.4 0 0 0 3.6.57 1 1 0 0 1 1 1V20a1 1 0 0 1-1 1A17 17 0 0 1 3 4a1 1 0 0 1 1-1h3.5a1 1 0 0 1 1 1c0 1.25.2 2.45.57 3.57a1 1 0 0 1-.25 1z"/></svg>
        Toll Free: 1-888-555-0142
      </div>
      <div class="topbar-register">Client Registration
        <svg width="20" height="10" viewBox="0 0 20 10"><path d="M0 5h18M14 1l4 4-4 4" stroke="#1b1b1b" stroke-width="1.2" fill="none"/></svg>
      </div>
      <nav class="main-nav">
        <a style="left:285px">Home</a><a style="left:353px">Services</a><a class="is-active" style="left:435px">Candidates</a><a style="left:529px">Employers</a><a style="left:620px">About Us</a><a style="left:703px">Contact Us</a>
      </nav>
    </header>
    <div class="hero hero--candidates" role="img" aria-label="Banner photos of workers in hard hats, a warehouse worker and an office professional">
      <h1 class="hero-title">CANDIDATES</h1>
    </div>

    <div class="photo photo--round" style="left:91px;top:316px;width:124px;height:124px;background:#8d7a6c" role="img" aria-label="Office professional holding a tablet"></div>
    <div class="photo photo--round" style="left:276px;top:309px;width:140px;height:140px;background:#5d6f86" role="img" aria-label="Worker in hi-vis vest walking through a factory"></div>
    <div class="photo photo--round" style="left:181px;top:421px;width:134px;height:134px;background:#7f7a52" role="img" aria-label="Warehouse worker with clipboard"></div>
    <div class="photo photo--round" style="left:84px;top:495px;width:94px;height:94px;background:#a08456" role="img" aria-label="Construction worker in hard hat"></div>
    <div class="photo photo--round" style="left:319px;top:500px;width:84px;height:84px;background:#4d5e74" role="img" aria-label="Offshore rig worker at sunset"></div>

    <h2 class="section-title" style="left:457px;top:377px">Your Career, Our<span class="accent">Priority</span></h2>
    <p class="body-copy" style="left:457px;top:417px;width:300px">For individuals seeking employment, a better job, consulting work, or &nbsp;freelance projects, we help you navigate toward career opportunities and lifestyle goals. To be leaders in our field, we need to be experts in &nbsp;yours. Candidates who work with us recognize that they get greater value with our dedicated expertise and support.</p>

    <h2 class="section-title" style="left:76px;top:648px">Registration &amp;<span class="accent">Placement</span></h2>
    <p class="body-copy" style="left:76px;top:687px;width:690px">By registering with us, Harbor Work Agency matches you with &nbsp;employers across Canada. The work may be temporary, temp-to-hire, contract, or permanent depending on the Employer needs. As a registered &nbsp;candidate, we continuously update your profile and help you stay on top &nbsp;of current opportunities.</p>

    <article class="placement-card" style="left:76px">
      <svg width="30" height="30" viewBox="0 0 30 30" fill="none" stroke="#e9ad08" stroke-width="1.6"><rect x="2" y="8" width="26" height="18" rx="2"/><path d="M10 8V4h10v4"/><circle cx="15" cy="18" r="5"/><path d="M15 15.5V18l2 1.5"/></svg>
      <h3>Temporary Placement</h3>
      <p>The opportunity to work for a specified period of time</p>
    </article>
    <article class="placement-card" style="left:311px">
      <svg width="30" height="30" viewBox="0 0 30 30" fill="none" stroke="#e9ad08" stroke-width="1.6"><rect x="2" y="6" width="20" height="16" rx="2"/><path d="M8 6V3h8v3M2 13h20"/><circle cx="23" cy="23" r="5.5"/><path d="M20.5 23l2 2 3-3.5"/></svg>
      <h3>Temporary-to-Hire</h3>
      <p>Showcase your skills, abilities, and commitment to the company leading to a permanent position</p>
    </article>
    <article class="placement-card" style="left:546px">
      <svg width="30" height="30" viewBox="0 0 30 30" fill="none" stroke="#e9ad08" stroke-width="1.6"><path d="M8 11a7 7 0 0 1 14 0z M6 11h18"/><path d="M9 13v3a6 6 0 0 0 12 0v-3"/><path d="M4 29v-3a6 6 0 0 1 6-5h10a6 6 0 0 1 6 5v3"/></svg>
      <h3>Permanent Placement</h3>
      <p>We will help you to find a permanent position according to your needs and expectations.</p>
    </article>
    <div class="apply-button">Apply Job</div>

    <div class="photo-frame" style="left:101px;top:973px;width:291px;height:309px"></div>
    <div class="photo" style="left:76px;top:948px;width:302px;height:320px;background:linear-gradient(180deg,#6f7a80 0%,#9a8a78 55%,#8a5a36 100%)" role="img" aria-label="Team of smiling colleagues around a table with laptops"></div>

    <h2 class="section-title" style="left:420px;top:974px">Connect with<span class="accent">HWA</span></h2>
    <div class="connect-badge" style="left:422px;top:1026px">
      <svg width="30" height="30" viewBox="0 0 30 30" fill="none" stroke="#1b1b1b" stroke-width="1.6"><rect x="5" y="3" width="13" height="24" rx="2"/><path d="M10 24h3"/><rect x="12" y="8" width="14" height="9" rx="2" fill="#f5c20f"/><path d="M16 12.5h.1M19 12.5h.1M22 12.5h.1" stroke-width="2"/></svg>
    </div>
    <h3 class="connect-title" style="top:1022px">Connect via Text</h3>
    <p class="connect-copy" style="top:1045px">Text <b>SUBSCRIBE</b> to <b>778-555-0193</b> (British Columbia) or <b>403-555-0177</b> (Alberta) to receive recurring automated promotional and personalized marketing text messages from Harbor Work Agency. Consent is not a condition of any purchase. Msg frequency varies. Msg &amp; data rates may apply. Reply HELP for help. Reply STOP to cancel.</p>
    <div class="connect-badge" style="left:422px;top:1175px">
      <svg width="30" height="30" viewBox="0 0 30 30" fill="none" stroke="#1b1b1b" stroke-width="1.6"><path d="M8 4h11l5 5v17H8z"/><path d="M19 4v5h5M12 14h8M12 18h8M12 22h5"/></svg>
    </div>
    <h3 class="connect-title" style="top:1165px">Our Policies</h3>
    <p class="connect-copy" style="top:1187px">Please visit our Privacy Policy and/or Terms and Conditions page for more details at <a>https://harborwork.ca/terms-of-use.</a></p>

    <footer class="site-footer" style="top:1320px">
      <span class="divider" style="left:226px"></span><span class="divider" style="left:398px"></span><span class="divider" style="left:571px"></span>
      <div class="footer-brand"><span class="brand-mark"></span><span class="brand-name">Harbor Work Agency Ltd.</span></div>
      <span class="social-dot" style="left:102px" aria-label="Social profile"></span><span class="social-dot" style="left:134px" aria-label="Social profile"></span>
      <h4 class="footer-heading" style="left:266px">Quick Links</h4>
      <ul class="footer-links" style="left:266px"><li>Home</li><li>Services</li><li>Candidates</li><li>Employers</li><li>About us</li><li>Contact us</li></ul>
      <h4 class="footer-heading" style="left:416px">Our Services</h4>
      <ul class="footer-links" style="left:416px"><li>Oil, Gas and Mining</li><li>Administrative</li><li>Construction and Trades</li><li>Warehouse and Logistics</li><li>Manufacturing.</li></ul>
      <h4 class="footer-heading" style="left:613px">Our Address</h4>
      <div class="footer-contact" style="top:92px"><svg width="18" height="22" viewBox="0 0 18 22" fill="none" stroke="#b8c3d6" stroke-width="1.2"><path d="M2 21V5l8-3v19M10 8h6v13M1 21h16M5 8h2M5 12h2M5 16h2M12 12h2M12 16h2"/></svg><span>410 Birchline Ave SW Calgary,<br>AB, T2P 4K9</span></div>
      <div class="footer-contact" style="top:133px"><svg width="16" height="16" viewBox="0 0 24 24" fill="none" stroke="#b8c3d6" stroke-width="1.5"><path d="M6.6 10.8a15.1 15.1 0 0 0 6.6 6.6l2.2-2.2a1 1 0 0 1 1-.25 11.4 11.4 0 0 0 3.6.57 1 1 0 0 1 1 1V20a1 1 0 0 1-1 1A17 17 0 0 1 3 4a1 1 0 0 1 1-1h3.5a1 1 0 0 1 1 1c0 1.25.2 2.45.57 3.57a1 1 0 0 1-.25 1z"/></svg><span>Toll-Free: 1-888-555-0142</span></div>
      <div class="footer-contact" style="top:159px"><svg width="16" height="16" viewBox="0 0 24 24" fill="none" stroke="#b8c3d6" stroke-width="1.5"><path d="M6.6 10.8a15.1 15.1 0 0 0 6.6 6.6l2.2-2.2a1 1 0 0 1 1-.25 11.4 11.4 0 0 0 3.6.57 1 1 0 0 1 1 1V20a1 1 0 0 1-1 1A17 17 0 0 1 3 4a1 1 0 0 1 1-1h3.5a1 1 0 0 1 1 1c0 1.25.2 2.45.57 3.57a1 1 0 0 1-.25 1z"/></svg><span>403-555-0177</span></div>
      <p class="copyright">© Harbor Work Agency Ltd. | All rights reserved 2026</p>
    </footer>
  </section>

  <!-- Employers page -->
  <section class="page page--employers">
    <header>
      <div class="brand"><span class="brand-mark"></span><span class="brand-name">Harbor Work Agency Ltd.</span></div>
      <div class="topbar-phone">
        <svg width="14" height="14" viewBox="0 0 24 24"><path fill="#fff" d="M6.6 10.8a15.1 15.1 0 0 0 6.6 6.6l2.2-2.2a1 1 0 0 1 1-.25 11.4 11.4 0 0 0 3.6.57 1 1 0 0 1 1 1V20a1 1 0 0 1-1 1A17 17 0 0 1 3 4a1 1 0 0 1 1-1h3.5a1 1 0 0 1 1 1c0 1.25.2 2.45.57 3.57a1 1 0 0 1-.25 1z"/></svg>
        Toll Free: 1-888-555-0142
      </div>
      <div class="topbar-register">Client Registration
        <svg width="20" height="10" viewBox="0 0 20 10"><path d="M0 5h18M14 1l4 4-4 4" stroke="#1b1b1b" stroke-width="1.2" fill="none"/></svg>
      </div>
      <nav class="main-nav">
        <a style="left:285px">Home</a><a style="left:353px">Services</a><a class="is-active" style="left:435px">Candidates</a><a style="left:529px">Employers</a><a style="left:620px">About Us</a><a style="left:703px">Contact Us</a>
      </nav>
    </header>
    <div class="hero hero--employers" role="img" aria-label="Business professionals standing in front of a city skyline at dusk">
      <h1 class="hero-title">EMPLOYERS</h1>
    </div>

    <h2 class="section-title" style="left:76px;top:299px">Strategic Staffing<span class="accent">Solutions</span></h2>
    <p class="body-copy" style="left:76px;top:339px;width:600px">We know that the success of every business relies upon having the finest employees.</p>

    <div class="photo-frame" style="left:119px;top:403px;width:293px;height:330px"></div>
    <div class="photo" style="left:76px;top:377px;width:323px;height:346px;background:linear-gradient(180deg,#c8d6e2 0%,#9fb3c4 50%,#4a9aa8 100%)" role="img" aria-label="Group of business people standing in a bright office"></div>

    <p class="body-copy" style="left:457px;top:387px;width:305px">For more than 10 years, Harbor Work Agency, &nbsp;has helped meet the staffing demands of business ranging from small one-person &nbsp;shops to Canada’s largest and most well-known Top 500 companies. We &nbsp;are proud of our record in developing and maintaining leading-edge &nbsp;staffing solutions that run the gamut from specialized national &nbsp;executive search, to massive labour force onboarding with a strong health &amp; safety focus.</p>
    <p class="body-copy" style="left:457px;top:545px;width:305px">At Harbor Work Agency, we listen to your staffing needs and develop a clear understanding of the candidates you are looking for. By &nbsp;drawing upon our extensive database of candidates and industry networks, our very knowledgeable and experienced project team will develop a &nbsp;customized staffing solution that meets your goals on-time and on budget.</p>
    <div class="register-button">Register With Us Now</div>

    <footer class="site-footer" style="top:762px">
      <span class="divider" style="left:226px"></span><span class="divider" style="left:398px"></span><span class="divider" style="left:571px"></span>
      <div class="footer-brand"><span class="brand-mark"></span><span class="brand-name">Harbor Work Agency Ltd.</span></div>
      <span class="social-dot" style="left:102px" aria-label="Social profile"></span><span class="social-dot" style="left:134px" aria-label="Social profile"></span>
      <h4 class="footer-heading" style="left:266px">Quick Links</h4>
      <ul class="footer-links" style="left:266px"><li>Home</li><li>Services</li><li>Candidates</li><li>Employers</li><li>About us</li><li>Contact us</li></ul>
      <h4 class="footer-heading" style="left:416px">Our Services</h4>
      <ul class="footer-links" style="left:416px"><li>Oil, Gas and Mining</li><li>Administrative</li><li>Construction and Trades</li><li>Warehouse and Logistics</li><li>Manufacturing.</li></ul>
      <h4 class="footer-heading" style="left:613px">Our Address</h4>
      <div class="footer-contact" style="top:92px"><svg width="18" height="22" viewBox="0 0 18 22" fill="none" stroke="#b8c3d6" stroke-width="1.2"><path d="M2 21V5l8-3v19M10 8h6v13M1 21h16M5 8h2M5 12h2M5 16h2M12 12h2M12 16h2"/></svg><span>410 Birchline Ave SW Calgary,<br>AB, T2P 4K9</span></div>
      <div class="footer-contact" style="top:133px"><svg width="16" height="16" viewBox="0 0 24 24" fill="none" stroke="#b8c3d6" stroke-width="1.5"><path d="M6.6 10.8a15.1 15.1 0 0 0 6.6 6.6l2.2-2.2a1 1 0 0 1 1-.25 11.4 11.4 0 0 0 3.6.57 1 1 0 0 1 1 1V20a1 1 0 0 1-1 1A17 17 0 0 1 3 4a1 1 0 0 1 1-1h3.5a1 1 0 0 1 1 1c0 1.25.2 2.45.57 3.57a1 1 0 0 1-.25 1z"/></svg><span>Toll-Free: 1-888-555-0142</span></div>
      <div class="footer-contact" style="top:159px"><svg width="16" height="16" viewBox="0 0 24 24" fill="none" stroke="#b8c3d6" stroke-width="1.5"><path d="M6.6 10.8a15.1 15.1 0 0 0 6.6 6.6l2.2-2.2a1 1 0 0 1 1-.25 11.4 11.4 0 0 0 3.6.57 1 1 0 0 1 1 1V20a1 1 0 0 1-1 1A17 17 0 0 1 3 4a1 1 0 0 1 1-1h3.5a1 1 0 0 1 1 1c0 1.25.2 2.45.57 3.57a1 1 0 0 1-.25 1z"/></svg><span>403-555-0177</span></div>
      <p class="copyright">© Harbor Work Agency Ltd. | All rights reserved 2026</p>
    </footer>
  </section>
</div>
</body>
</html>
```